Lydia Vandermere personal business/name cards and stationery brief

I am looking for a simple design on my personal business cards, that I may use for all my stationery. All my stationery would be cream or ivory textured card, or cream/ivory quality paper. I am director of my family company and also property developer. But am wishing to have basic business cards that I can use across both businesses. I do not wish to have a title, just my initials as a focal point.
Target Market(s)
These are my personal business cards and stationery. I am looking for an elegant, relatively understated design that exudes wealth. There is no target audience, other than clients or people I already do business with. However design must be stylish and timeless.
If I am handing out my business card to anyone I do not do business with, or they are not contracting to me or my company currently, then i would like the target audience to wish they were.
I am 54 yeas of age, and my business cards must denote respect and class.
Industry/Entity Type
Business
Contact Information for Business Card
LV
Lydia Vandermere
Justice of the Peace
Possible rear of card
Mobile number
Email
Font styles to use
Requirements
Must have
- LV to be somehow entwined as a logo on the front of the card above my name
- These cards must state that I am a Justice of the Peace
- Colours only ivory or cream card with texture, and gold elegant font.
- Must be able to be used on all my stationery products
- Must be elegant, timeless and not cluttered
- Below are just some design I like. There is something in each design I like.
Nice to have
- I would like my initials to be the centre piece of the card. Somehow entwined together elegantly in a logo of sorts that I can use across all my stationery. But if not my initials, then something that is different and stands out from the rest.
Should not have
- Not gawdy or young. No colour. Nothing outlandish.

```html
<!DOCTYPE html>
<html lang="en">
<head>
<meta charset="utf-8">
<title>Lydia Vandermere — Business Card</title>
<link rel="stylesheet" href="https://fonts.googleapis.com/css2?family=Exo+2:wght@300;400&display=swap">
<style>
  :root {
    --page-bg: #dcdad4;
    --gold: #8f6b22;
    --gold-soft: #b08d44;
    --ivory-light: #fffdf4;
    --ivory-mid: #faf3dc;
    --ivory-deep: #f1e6c4;
    --paper: #fbf8ee;
    --paper-edge: #fffefa;
  }
  * { box-sizing: border-box; margin: 0; padding: 0; }
  html, body {
    width: 1200px;
    height: 1200px;
    overflow: hidden;
    background: var(--page-bg);
    font-family: "Exo 2", sans-serif;
    color: var(--gold);
  }
  .sheet {
    width: 1200px;
    height: 1200px;
    display: flex;
    flex-direction: column;
    align-items: center;
    justify-content: center;
    gap: 80px;
  }
  .card {
    width: 760px;
    height: 434px;
    position: relative;
    box-shadow: 0 6px 18px rgba(0,0,0,0.16);
  }

  /* Front */
  .card-front {
    background: radial-gradient(ellipse at 55% 60%, var(--ivory-light) 0%, var(--ivory-mid) 60%, var(--ivory-deep) 100%);
    display: flex;
    flex-direction: column;
    align-items: center;
    padding-top: 62px;
  }
  .monogram {
    display: flex;
    align-items: center;
    gap: 16px;
    height: 130px;
  }
  .monogram-mark {
    width: 14px;
    height: 14px;
    border-radius: 50%;
    background: var(--gold);
  }
  .monogram-name {
    font-size: 96px;
    font-weight: 400;
    letter-spacing: 4px;
    line-height: 1;
    color: var(--gold);
  }
  .holder-name {
    margin-top: 30px;
    font-size: 46px;
    font-weight: 400;
    letter-spacing: 3px;
    text-transform: uppercase;
  }
  .holder-role {
    margin-top: 10px;
    font-size: 26px;
    font-weight: 300;
    letter-spacing: 2px;
  }
  .front-rule {
    margin-top: 26px;
    width: 150px;
    height: 2px;
    background: var(--gold);
  }

  /* Back */
  .card-back {
    background: var(--paper);
    border: 18px solid var(--paper-edge);
  }
  .frame-outer {
    position: absolute;
    inset: 14px;
    border: 2px solid var(--gold-soft);
  }
  .frame-inner {
    position: absolute;
    inset: 22px;
    border: 1px solid var(--gold-soft);
  }
  .contact {
    position: absolute;
    inset: 0;
    display: flex;
    flex-direction: column;
    align-items: center;
    justify-content: center;
    font-weight: 300;
    letter-spacing: 1.5px;
    font-size: 26px;
  }
  .contact-email { margin-top: 8px; }
  .contact-divider {
    position: relative;
    width: 340px;
    height: 1px;
    background: var(--gold-soft);
    margin: 24px 0;
  }
  .contact-divider::after {
    content: "";
    position: absolute;
    left: 50%;
    top: 50%;
    width: 6px;
    height: 6px;
    border-radius: 50%;
    background: var(--gold);
    transform: translate(-50%, -50%);
  }
</style>
</head>
<body>
  <main class="sheet">
    <section class="card card-front" aria-label="Card front">
      <div class="monogram">
        <span class="monogram-mark" aria-hidden="true"></span>
        <span class="monogram-name">LV</span>
      </div>
      <h1 class="holder-name">Lydia Vandermere</h1>
      <p class="holder-role">Justice of the Peace</p>
      <div class="front-rule" aria-hidden="true"></div>
    </section>

    <section class="card card-back" aria-label="Card back">
      <div class="frame-outer" aria-hidden="true"></div>
      <div class="frame-inner" aria-hidden="true"></div>
      <div class="contact">
        <p class="contact-phone">1-234-567890</p>
        <p class="contact-email">john@companyname.com</p>
        <div class="contact-divider" aria-hidden="true"></div>
        <p class="contact-address">Dummy city, Dummy Country Land</p>
      </div>
    </section>
  </main>
</body>
</html>
```